A flyer for future customers to get acquainted with our company

The flyer/card is intended for intermediaries. The purpose of this flyer is to introduce businesses to Dovrel.

It should convey: real estate and financing, with actual images. Various keywords describing what we do: project financing, temporary real estate financing, real estate financing, investment properties, transformations. We distinguish ourselves by being fast, flexible, and personal.

Please ensure the front has an attractive and inviting appearance, and leave space on the back for additional text.

Color codes: #E85B35 en #091E33

```html
<!DOCTYPE html>
<html lang="en">
<head>
<meta charset="utf-8">
<title>Dovrel – Real Estate and Financing Postcard</title>
<link href="https://fonts.googleapis.com/css2?family=Heebo:wght@700;800&family=Montserrat:wght@400;500&family=Oswald:wght@600&display=swap" rel="stylesheet">
<style>
  :root {
    --orange: #E85B35;
    --navy: #091E33;
    --white: #ffffff;
    --ink: #111111;
    --rule: #555555;
    --canvas: #eef0f3;
  }
  * { margin: 0; padding: 0; box-sizing: border-box; }
  html, body { width: 1199px; height: 1200px; overflow: hidden; background: var(--canvas); }
  .canvas { position: relative; width: 1199px; height: 1200px; }

  .card {
    position: absolute;
    left: 226px;
    width: 746px;
    height: 527px;
    background: var(--white);
    overflow: hidden;
  }
  .card--front { top: 54px; }
  .card--back { top: 617px; }
  .card svg.shapes { position: absolute; inset: 0; }

  .headline {
    position: absolute;
    left: 60px;
    width: 340px;
    top: 76px;
    text-align: center;
    font-family: "Heebo", sans-serif;
    font-weight: 800;
    line-height: 1.1;
  }
  .headline__accent { display: block; color: var(--orange); font-size: 45px; }
  .headline__main { display: block; color: var(--ink); font-size: 40px; line-height: 1.3; }

  .brand {
    position: absolute;
    font-family: "Heebo", sans-serif;
    font-weight: 800;
    color: var(--navy);
    letter-spacing: -0.5px;
    display: flex;
    align-items: center;
    gap: 8px;
  }
  .brand__dot { width: 12px; height: 12px; border-radius: 50%; background: var(--orange); }
  .card--front .brand { right: 38px; top: 44px; font-size: 56px; line-height: 1; }
  .card--back .brand { left: 46px; top: 44px; font-size: 48px; line-height: 1; }

  .contact {
    position: absolute;
    right: 32px;
    top: 136px;
    text-align: right;
    font-family: "Montserrat", sans-serif;
    font-weight: 500;
    font-size: 13.5px;
    line-height: 17px;
    color: var(--navy);
    list-style: none;
  }

  .services { position: absolute; left: 37px; top: 393px; color: var(--white); }
  .services__title {
    font-family: "Oswald", sans-serif;
    font-weight: 600;
    font-size: 27px;
    letter-spacing: 0.5px;
    margin-bottom: 10px;
  }
  .services__list {
    font-family: "Montserrat", sans-serif;
    font-weight: 400;
    font-size: 15.5px;
    line-height: 20px;
  }

  .back-title {
    position: absolute;
    left: 46px;
    top: 414px;
    color: var(--white);
    font-family: "Heebo", sans-serif;
    font-weight: 700;
    line-height: 1.1;
  }
  .back-title__main { display: block; font-size: 36px; }
  .back-title__sub { display: block; font-size: 28px; }

  .stamp-box {
    position: absolute;
    left: 629px; top: 44px;
    width: 85px; height: 101px;
    border: 1.5px solid var(--rule);
  }
  .address-line {
    position: absolute;
    left: 444px;
    width: 270px;
    height: 0;
    border-top: 1.5px solid var(--rule);
  }
</style>
</head>
<body>
<main class="canvas">

  <section class="card card--front">
    <svg class="shapes" width="746" height="527" viewBox="0 0 746 527">
      <defs>
        <linearGradient id="meeting-tones" x1="0" y1="0" x2="1" y2="1">
          <stop offset="0" stop-color="#b9b3a8"/>
          <stop offset="0.45" stop-color="#dfe3e8"/>
          <stop offset="0.75" stop-color="#7d8796"/>
          <stop offset="1" stop-color="#4c5563"/>
        </linearGradient>
      </defs>
      <path d="M0,300 C188,312 375,350 525,425 C650,475 719,500 706,527 L0,527 Z" fill="var(--orange)"/>
      <circle cx="230" cy="134" r="225" fill="var(--navy)"/>
      <circle cx="230" cy="152" r="170" fill="var(--white)"/>
      <circle cx="536" cy="296" r="177" fill="var(--white)"/>
      <circle cx="536" cy="296" r="174" fill="url(#meeting-tones)" role="img" aria-label="Photo of business people reviewing financial charts at a desk"/>
    </svg>

    <h1 class="headline">
      <span class="headline__accent">Real Estate</span>
      <span class="headline__main">and<br>Financing</span>
    </h1>

    <div class="brand"><span>Dovrel</span><span class="brand__dot"></span></div>

    <ul class="contact">
      <li>0612 348 905</li>
      <li>hello@dovrelfinance.com</li>
      <li>www.dovrelfinance.com</li>
    </ul>

    <div class="services">
      <h2 class="services__title">WHAT WE DO:</h2>
      <p class="services__list">Project financing, temporary real estate financing,<br>real estate financing, investment properties, transformations.</p>
    </div>
  </section>

  <section class="card card--back">
    <svg class="shapes" width="746" height="527" viewBox="0 0 746 527">
      <defs>
        <linearGradient id="skyline-tones" x1="0" y1="0" x2="0" y2="1">
          <stop offset="0" stop-color="#2f3a47"/>
          <stop offset="0.5" stop-color="#4a5766"/>
          <stop offset="1" stop-color="#27313d"/>
        </linearGradient>
      </defs>
      <circle cx="175" cy="338" r="194" fill="var(--orange)"/>
      <circle cx="144" cy="356" r="181" fill="url(#skyline-tones)" role="img" aria-label="Photo of a businessman looking out over a city skyline"/>
      <circle cx="136" cy="432" r="138" fill="var(--white)" fill-opacity="0.16"/>
    </svg>

    <div class="brand"><span>Dovrel</span><span class="brand__dot"></span></div>

    <h2 class="back-title">
      <span class="back-title__main">Real Estate</span>
      <span class="back-title__sub">and Financing</span>
    </h2>

    <div class="stamp-box"></div>
    <div class="address-line" style="top:204px"></div>
    <div class="address-line" style="top:248px"></div>
    <div class="address-line" style="top:292px"></div>
    <div class="address-line" style="top:336px"></div>
  </section>

</main>
</body>
</html>
```